Business Card Design for BrightlaneReach.com

--I need a business card design for my company BrightlaneReach.com

I have attached my logo...I want the brightlane reach logo on the front of the business card, and then I want The Brightlane Chief on the back of it with my information.

I would like to see a light colored background as well as a dark colored background

FRONT:
BRIGHTLANE REACH LOGO
247 E. Pelham Row
5th Floor
San Diego CA 92384
www.BrightlaneReach.com

Advanced Website & App Development
Websites, Apps, Online Voucher Systems

Leading Edge Marketing Services
SMS, VB, SMM, SEM,

BACK:
BRIGHTLANE CHIEF LOGO
Dorian Welker
The Brightlane Chief
Call Or Text: 555-204-3378
Dorian@BrightlaneChief.com
www.BrightlaneChief.com

Target Market(s)

small business owners

Industry/Entity Type

Business Consultant

Contact Information for Business Card

FRONT:
BRIGHTLANE REACH LOGO
247 E. Pelham Row
5th Floor
San Diego CA 92384
www.BrightlaneReach.com

SMS, VB, SMM, SEM,

BACK:
BRIGHTLANE CHIEF LOGO
Dorian Welker
The Brightlane Chief
Dorian@BrightlaneChief.com
www.BrightlaneChief.com

Requirements
Must have
• add this quote on it somewhere, anywhere,preferrably on back
• "The Fastest Way To Success Is To Take Action”
• — Dorian Welker, Brightlane Chief
Nice to have
• open
Should not have
• red

```html
<!DOCTYPE html>
<html lang="en">
<head>
<meta charset="utf-8">
<title>Brightlane Reach – Business Cards</title>
<link rel="stylesheet" href="https://fonts.googleapis.com/css2?family=Lato:ital,wght@0,300;0,400;0,700;1,400&display=swap">
<style>
  :root {
    --backdrop: #3a3a3a;
    --card: #ffffff;
    --brand-blue: #0b6fa3;
    --text-blue: #1779b0;
    --text-grey: #5a5a5a;
    --band-text: #ffffff;
  }
  * { box-sizing: border-box; margin: 0; padding: 0; }
  html, body {
    width: 1200px; height: 900px; overflow: hidden;
    background: var(--backdrop);
    font-family: "Lato", Arial, sans-serif;
  }
  .stage { position: relative; width: 1200px; height: 900px; }
  .card {
    position: absolute; top: 301px;
    width: 514px; height: 296px;
    background: var(--card);
    overflow: hidden;
  }
  .card--front { left: 72px; }
  .card--back { left: 615px; }
  .brand-name {
    position: absolute; left: 43px; top: 44px;
    font-size: 30px; font-weight: 400; letter-spacing: 2px;
    color: var(--brand-blue); line-height: 1;
    white-space: nowrap;
  }
  .services {
    position: absolute; left: 43px; top: 124px;
    list-style: none;
    font-size: 20px; font-weight: 300; line-height: 24.5px;
    color: var(--text-blue);
  }
  .address {
    position: absolute; left: 323px; top: 162px;
    font-style: normal; font-size: 11.5px; line-height: 14.5px;
    color: var(--text-grey);
  }
  .band {
    position: absolute; left: 0; right: 0; bottom: 0;
    height: 71px; background: var(--brand-blue);
    color: var(--band-text);
  }
  .band__lines {
    position: absolute; left: 43px; top: 11px;
    font-size: 19.5px; font-weight: 300; line-height: 24.5px;
  }
  .person { position: absolute; left: 43px; top: 129px; font-size: 12.5px; line-height: 16px; }
  .person__name { font-weight: 700; color: var(--text-blue); }
  .person__title { color: var(--text-grey); }
  .contacts {
    position: absolute; left: 43px; top: 175px;
    list-style: none; font-size: 12.5px; line-height: 16px; color: var(--text-grey);
  }
  .contacts li { display: flex; align-items: center; gap: 6px; }
  .contacts svg { width: 11px; height: 11px; fill: var(--brand-blue); }
  .quote {
    position: absolute; left: 43px; top: 11px;
    font-size: 19.5px; font-weight: 300; line-height: 24.5px;
  }
  .quote__attribution {
    position: absolute; right: 83px; top: 42px;
    font-size: 12px;
  }
  .quote__attribution strong { font-weight: 700; }
  .quote__attribution em { font-style: italic; }
</style>
</head>
<body>
<main class="stage">

  <section class="card card--front" aria-label="Front of card">
    <div class="brand-name">BRIGHTLANE REACH</div>
    <ul class="services">
      <li>Advanced Website &amp; App</li>
      <li>Development</li>
      <li>Websites, Apps</li>
      <li>Online Voucher Systems</li>
    </ul>
    <address class="address">
      247 E. Pelham Row<br>
      5th Floor<br>
      San Diego CA 92384<br>
      www.BrightlaneReach.com
    </address>
    <div class="band">
      <p class="band__lines">Leading Edge Marketing Services<br>SMS, VB, SMM, SEM</p>
    </div>
  </section>

  <section class="card card--back" aria-label="Back of card">
    <div class="brand-name">BRIGHTLANE CHIEF</div>
    <div class="person">
      <p class="person__name">Dorian Welker</p>
      <p class="person__title">The Brightlane Chief</p>
    </div>
    <ul class="contacts">
      <li>
        <svg viewBox="0 0 12 12" aria-hidden="true"><path d="M1 5c0-2 2.5-3 5-3s5 1 5 3l-2 .8-.7-1.5H3.7L3 5.8z"/><rect x="3" y="6.5" width="6" height="3.5" rx="1"/></svg>
        555-204-3378
      </li>
      <li>
        <svg viewBox="0 0 12 12" aria-hidden="true"><path d="M1 3h10v1L6 7 1 4z"/><path d="M1 5.2l5 3 5-3V10H1z"/></svg>
        Dorian@BrightlaneChief.com
      </li>
      <li>
        <svg viewBox="0 0 12 12" aria-hidden="true"><path d="M6 1a5 5 0 1 0 0 10A5 5 0 0 0 6 1zm0 1c.7.8 1.2 2 1.3 3.5H4.7C4.8 4 5.3 2.8 6 2zM2.1 6.5h1.6c.1 1.3.5 2.5 1 3.3A4 4 0 0 1 2.1 6.5zm0-1A4 4 0 0 1 4.7 2.2c-.5.8-.9 2-1 3.3zm2.6 1h2.6C7.2 8 6.7 9.2 6 10c-.7-.8-1.2-2-1.3-3.5zm3.6 0h1.6a4 4 0 0 1-2.6 3.3c.5-.8.9-2 1-3.3zm0-1c-.1-1.3-.5-2.5-1-3.3a4 4 0 0 1 2.6 3.3z"/></svg>
        www.BrightlaneChief.com
      </li>
    </ul>
    <div class="band">
      <p class="quote">The Fastest Way To Success Is To Take Action</p>
      <p class="quote__attribution">— <strong>Dorian Welker</strong>, <em>Brightlane Chief</em></p>
    </div>
  </section>

</main>
</body>
</html>
```